New Meal Prep Flyer for New Package Deals

We are looking for a design that displays our new packages that we offer. If you take a look at our website www.copperspoonpantry.com, and click on packages , you'll see the way we display them currently . We would like something similar to that in style . The first package is called "Evergreen" and this package will be a 1 week package (7 days ), 2 meals a day, for a price of $195.00. The second package is called "Pebble" and this package will be a 3 week package (21 days) 2 meals per day, for a price of $546.00 , the third package is a 6 week+ package (45 days), and it is called "Lighthouse" , 2 meals per day , and the price is $1080.00 .
For the Pebble Package , can you put next to it "Save $42.00!"
For the Lighthouse Package, can you put next to it "Save $180!"
We also want our logo on the flyer (see attached), and we are just looking for a 1 page flyer , 8 1/2 x 11.

```html
<!DOCTYPE html>
<html lang="en">
<head>
<meta charset="utf-8">
<title>Copper Spoon Pantry – Meal Prep Packages</title>
<link rel="stylesheet" href="https://fonts.googleapis.com/css2?family=Oswald:wght@400;500;600;700&family=Roboto+Condensed:wght@400;700;800&display=swap">
<style>
  :root {
    --green: #8cc43f;
    --navy: #14305a;
    --grey-logo: #6f6f73;
    --paper: #f4f1f2;
    --cream: #eeefd8;
    --card: #f7f6fb;
    --card-alt: #d9dadd;
    --coupon: #a3a4a8;
    --text-navy: #1b3157;
    --page-bg: #e6e6e6;
  }
  * { box-sizing: border-box; margin: 0; padding: 0; }
  html, body { width: 1200px; height: 800px; overflow: hidden; }
  body { background: var(--page-bg); font-family: "Roboto Condensed", sans-serif; position: relative; }

  .flyer { position: absolute; left: 300px; top: 12px; width: 600px; height: 776px; background: var(--paper); overflow: hidden; box-shadow: 0 2px 10px rgba(0,0,0,.15); }

  .brand { position: absolute; left: 0; top: 0; width: 100%; height: 100px; display: flex; align-items: center; padding-left: 40px; gap: 12px; }
  .brand-dot { width: 22px; height: 22px; border-radius: 50%; background: var(--green); flex: none; }
  .brand-name { font-family: "Oswald", sans-serif; font-weight: 700; font-size: 44px; letter-spacing: 1px; color: var(--grey-logo); text-transform: uppercase; white-space: nowrap; }

  .food-photo { position: absolute; left: 0; top: 100px; width: 100%; height: 460px;
    background: radial-gradient(ellipse at 40% 35%, #7a7d7f 0%, #5a5f63 45%, #3e4347 100%); }

  .panel { position: absolute; left: 0; top: 560px; width: 100%; height: 140px; background: var(--cream); }

  .packages { position: absolute; left: 24px; top: 420px; width: 552px; height: 280px; display: flex; align-items: flex-end; }
  .package { position: relative; flex: 1; display: flex; flex-direction: column; height: 100%; }
  .package--evergreen { padding-top: 70px; }
  .package--pebble { padding-top: 35px; }
  .package--lighthouse { padding-top: 0; }

  .badge { position: absolute; left: 50%; transform: translateX(-50%); width: 60px; height: 60px; border-radius: 50%; background: var(--navy); border: 4px solid #fff; box-shadow: 0 0 0 2px var(--navy); z-index: 2; }
  .badge--green { background: var(--green); box-shadow: 0 0 0 2px var(--green); }
  .badge::after { content: ""; position: absolute; inset: 13px; border-radius: 50%; border: 2px solid #fff; }
  .package--evergreen .badge { top: 8px; }
  .package--pebble .badge { top: -27px; }
  .package--lighthouse .badge { top: -62px; }

  .package-head { height: 44px; display: flex; align-items: flex-end; justify-content: center; padding-bottom: 4px; font-family: "Oswald", sans-serif; font-weight: 700; font-size: 23px; line-height: 1; color: #fff; text-transform: uppercase; letter-spacing: .5px; }
  .head--green { background: var(--green); }
  .head--navy { background: var(--navy); }

  .package-body { flex: 1; background: var(--card); border: 2px solid var(--navy); border-top: none; text-align: center; color: var(--text-navy); padding: 10px 6px 0; display: flex; flex-direction: column; align-items: center; }
  .package--pebble .package-body { background: var(--card-alt); }
  .length { font-weight: 800; font-size: 16px; text-transform: uppercase; }
  .days { font-size: 13px; margin-bottom: 6px; }
  .meals { font-size: 13px; text-transform: uppercase; font-weight: 700; }
  .price-lead { font-size: 13px; }
  .price { font-family: "Oswald", sans-serif; font-weight: 600; font-size: 26px; line-height: 1.1; }
  .save { margin-top: 8px; width: 140px; padding: 5px 0; background: var(--coupon); outline: 2px dashed var(--coupon); outline-offset: 3px; color: #fff; font-family: "Oswald", sans-serif; font-size: 18px; }

  .footer { position: absolute; left: 0; bottom: 0; width: 100%; height: 76px; background: var(--navy); display: flex; align-items: center; padding: 0 18px; gap: 14px; }
  .cta { background: var(--green); color: var(--navy); font-family: "Oswald", sans-serif; font-weight: 700; font-size: 17px; padding: 8px 12px; display: flex; align-items: center; gap: 7px; white-space: nowrap; flex: none; }
  .cta svg { width: 18px; height: 18px; }
  .web { color: #fff; font-size: 13px; line-height: 1.4; white-space: nowrap; }
  .web-url { color: var(--green); font-weight: 700; display: flex; align-items: center; gap: 5px; }
  .web-url svg { width: 13px; height: 13px; }
</style>
</head>
<body>
  <main class="flyer">
    <header class="brand">
      <span class="brand-dot"></span>
      <span class="brand-name">Copper Spoon Pantry</span>
    </header>

    <div class="food-photo" role="img" aria-label="Photo of five sealed meal prep trays with chicken, vegetables and pasta on a dark slate surface"></div>

    <div class="panel"></div>

    <section class="packages">
      <article class="package package--evergreen">
        <span class="badge"></span>
        <h2 class="package-head head--green">Evergreen</h2>
        <div class="package-body">
          <p class="length">1 Week Package</p>
          <p class="days">(7 days),</p>
          <p class="meals">2 Meals a Day,</p>
          <p class="price-lead">For a price of</p>
          <p class="price">$195.00</p>
        </div>
      </article>
      <article class="package package--pebble">
        <span class="badge badge--green"></span>
        <h2 class="package-head head--navy">Pebble</h2>
        <div class="package-body">
          <p class="length">3 Week Package</p>
          <p class="days">(21 days)</p>
          <p class="meals">2 Meals per Day,</p>
          <p class="price-lead">For a price of</p>
          <p class="price">$546.00</p>
          <p class="save">Save $42.00!</p>
        </div>
      </article>
      <article class="package package--lighthouse">
        <span class="badge"></span>
        <h2 class="package-head head--green">Lighthouse</h2>
        <div class="package-body">
          <p class="length">6 Week+ Package</p>
          <p class="days">(45 days)</p>
          <p class="meals">2 Meals per Day,</p>
          <p class="price-lead">For a price of</p>
          <p class="price">$1080.00</p>
          <p class="save">Save $180!</p>
        </div>
      </article>
    </section>

    <footer class="footer">
      <div class="cta">
        CALL TO ORDER TODAY!
        <svg viewBox="0 0 24 24" aria-hidden="true"><circle cx="12" cy="12" r="11" fill="none" stroke="#14305a" stroke-width="2"/><path d="M8 6.5l2 0 1 3-1.5 1a7 7 0 0 0 4 4l1-1.5 3 1v2a1.5 1.5 0 0 1-1.5 1.5A10 10 0 0 1 6.5 8 1.5 1.5 0 0 1 8 6.5z" fill="#14305a"/></svg>
        1-555-014-2287
      </div>
      <div class="web">
        <p>You can find more info on our website</p>
        <p class="web-url">
          <svg viewBox="0 0 16 16" aria-hidden="true"><circle cx="8" cy="8" r="7" fill="none" stroke="#8cc43f" stroke-width="1.5"/><path d="M1 8h14M8 1c3 3 3 11 0 14M8 1c-3 3-3 11 0 14" fill="none" stroke="#8cc43f" stroke-width="1.2"/></svg>
          www.copperspoonpantry.com
        </p>
      </div>
    </footer>
  </main>
</body>
</html>
```